Market online tutoring + Back to School + give Support for students school work K to 12 Grade

To promote my tutoring business online need to create a two sided flyer. Need to get the attention of parents and educators who looking for help to support the digital learning of their students due to COVID-19 lock down. I need to project and differentiate that we offer support for online school with individualized learning . We tutor Elementary to High school students on all subjects you may take a look at my website qnacademyga.com for additional info and also I can provide
Updates

Hi All Due to Covid, we were unable to work on this project on time as originally planned. We were given an extension until March 15 and we will complete it by then. Sorry for any inconvenience and Thank you for your support. -QN Academy

Target Market(s)

Parents and students

Industry/Entity Type

Education

Requirements
Must have
• For online less fine print on the first page. The phone number and support text message. Back to School , Support Online learning KEV/NUR test prep should have some focus
Nice to have
• Discuss the platform We created a platform with live instructor interaction, virtual classroom, instructional videos, assessments, and practice to support every individual student’s need. We are confident in our ability to provide the most effective distance learning experience.
Should not have
• too much clunky and packed with content. Should be easy to read with color

```html
<!DOCTYPE html>
<html lang="en">
<head>
<meta charset="utf-8">
<title>QN Academy – Online Tutoring K to 12</title>
<link href="https://fonts.googleapis.com/css2?family=Montserrat:wght@400;500;600;700;800&family=Roboto+Slab:wght@700;800&display=swap" rel="stylesheet">
<style>
  :root{
    --red:#b7141d;
    --red-bright:#d01f26;
    --navy:#1f2b3d;
    --slate:#2c3a4d;
    --white:#ffffff;
    --ink:#1b2433;
  }
  *{margin:0;padding:0;box-sizing:border-box}
  html,body{width:1200px;height:2260px;overflow:hidden;background:var(--white)}
  .flyer{position:relative;width:1200px;height:2260px;overflow:hidden;background:var(--white);font-family:'Montserrat',sans-serif;color:var(--ink)}
  .abs{position:absolute;white-space:nowrap}

  .hero-photo{left:430px;top:0;width:770px;height:1010px;
    background:radial-gradient(ellipse at 60% 35%,#d9c7c4 0%,#c6b3b4 30%,#9a8c92 60%,#e4e4e6 100%)}
  .hero-fade{left:380px;top:0;width:260px;height:1010px;background:linear-gradient(90deg,#fff 0%,rgba(255,255,255,0) 100%)}

  .headline{left:56px;top:40px;font-family:'Roboto Slab',serif;font-weight:800;color:var(--red);line-height:1}
  .headline .l1{font-size:180px;letter-spacing:2px}
  .headline .l2{font-size:140px;margin-top:6px}

  .audience{left:62px;top:395px;color:var(--navy);font-weight:800;line-height:1}
  .audience .for{font-weight:600;font-size:52px}
  .audience .grade{font-size:118px;margin-top:14px;letter-spacing:-1px}
  .covid{left:62px;top:735px;background:var(--red);color:var(--white);font-weight:700;font-size:52px;padding:8px 22px}
  .lockdown{left:62px;top:835px;color:var(--navy);font-weight:800;font-size:70px}

  .badge{left:860px;top:660px;width:300px;height:300px;border-radius:50%;background:var(--red-bright);color:var(--white);
    display:flex;flex-direction:column;align-items:center;justify-content:center;text-align:center;font-weight:800;line-height:1.05;
    box-shadow:0 6px 16px rgba(0,0,0,.25);transform:rotate(-6deg)}
  .badge .s{font-size:38px}
  .badge .b{font-size:62px;margin:6px 0}

  .tab{left:110px;top:1010px;width:700px;height:82px;background:var(--red-bright);border-radius:26px 26px 0 0;
    color:var(--white);font-weight:600;font-size:44px;line-height:82px;text-align:center}

  .platform{left:0;top:1092px;width:1200px;height:528px;background:var(--slate);color:var(--white)}
  .feature{position:absolute;left:90px;display:flex;align-items:center;gap:26px;font-weight:800;font-size:48px;letter-spacing:.3px;white-space:nowrap;line-height:1}
  .feature svg{width:64px;height:64px;flex:none}
  .f1{top:44px}.f2{top:150px}.f3{top:256px}.f4{top:362px}
  .support-note{position:absolute;left:180px;top:450px;font-weight:500;font-size:32px;white-space:nowrap}

  .promise{left:0;top:1620px;width:1200px;height:150px;background:var(--red);color:var(--white);
    font-weight:800;font-size:40px;line-height:1.3;text-align:center;display:flex;align-items:center;justify-content:center}

  .brand{left:70px;top:1830px;display:flex;align-items:center;gap:26px}
  .brand .mark{width:100px;height:100px;background:var(--navy)}
  .brand .name{font-weight:800;font-size:64px;color:var(--navy)}
  .divider{left:700px;top:1815px;width:3px;height:150px;background:var(--navy)}
  .stay{left:735px;top:1830px;display:flex;align-items:center;gap:18px;font-weight:800;font-size:44px;line-height:1.1}
  .stay .home{color:var(--navy)}
  .stay .safe{color:var(--red)}

  .join{left:290px;top:1998px;width:620px;height:74px;border-radius:37px;background:var(--navy);color:var(--white);
    font-weight:700;font-size:36px;line-height:74px;text-align:center}
  .web{left:0;top:2086px;width:1200px;text-align:center;color:var(--red);font-weight:800;font-size:68px;line-height:1.1}
  .phone{left:0;top:2170px;width:1200px;text-align:center;color:var(--navy);font-weight:500;font-size:66px;line-height:1.1}
</style>
</head>
<body>
<main class="flyer">
  <div class="abs hero-photo" role="img" aria-label="Photo of a student wearing headphones and a face mask studying at a laptop with notebooks and pencils"></div>
  <div class="abs hero-fade"></div>

  <h1 class="abs headline"><div class="l1">ONLINE</div><div class="l2">TUTORING</div></h1>

  <div class="abs audience">
    <div class="for">for students</div>
    <div class="grade">K TO 12<br>GRADE</div>
  </div>
  <div class="abs covid">due to COVID-19</div>
  <div class="abs lockdown">LOCKDOWN</div>

  <div class="abs badge"><span class="s">WE OFFER</span><span class="b">KEV/NUR</span><span class="s">TEST PREP.</span></div>

  <div class="abs tab">We created a platform with...</div>

  <section class="abs platform">
    <div class="feature f1">
      <svg viewBox="0 0 70 70" fill="none" stroke="#fff" stroke-width="4"><rect x="6" y="10" width="58" height="38" rx="4"/><circle cx="35" cy="26" r="7"/><path d="M24 42c3-6 19-6 22 0M20 60h30M35 48v12"/></svg>
      <span>LIVE INSTRUCTOR INTERACTION</span>
    </div>
    <div class="feature f2">
      <svg viewBox="0 0 70 70" fill="none" stroke="#fff" stroke-width="4"><rect x="6" y="10" width="58" height="38" rx="4"/><circle cx="22" cy="26" r="5"/><circle cx="48" cy="26" r="5"/><path d="M14 40c2-5 14-5 16 0M40 40c2-5 14-5 16 0M20 60h30"/></svg>
      <span>VIRTUAL CLASSROOM</span>
    </div>
    <div class="feature f3">
      <svg viewBox="0 0 70 70" fill="none" stroke="#fff" stroke-width="4"><rect x="6" y="12" width="58" height="40" rx="4"/><path d="M29 23l14 9-14 9z" fill="#fff"/><path d="M20 62h30"/></svg>
      <span>ANSTRUCTIONAL VIDEOS</span>
    </div>
    <div class="feature f4">
      <svg viewBox="0 0 70 70" fill="none" stroke="#fff" stroke-width="4"><rect x="12" y="6" width="46" height="58" rx="4"/><path d="M22 22l4 4 8-8M22 40l4 4 8-8M40 22h10M40 40h10"/></svg>
      <span>ASSESSMENTS, AND PRACTICE</span>
    </div>
    <p class="support-note">to support every individual student’s need.</p>
  </section>

  <div class="abs promise">We are confident in our ability to provide the<br>most effective distance learning experience.</div>

  <div class="abs brand"><span class="mark"></span><span class="name">QN Academy</span></div>
  <div class="abs divider"></div>
  <div class="abs stay">
    <svg width="80" height="80" viewBox="0 0 90 90" fill="none" stroke="#1f2b3d" stroke-width="6"><path d="M8 44L45 12l37 32M18 36v44h54V36"/><rect x="38" y="54" width="14" height="26"/></svg>
    <div><div class="home">STAY HOME</div><div class="safe">STAY SAFE</div></div>
  </div>

  <div class="abs join">Join Online Classes Today !</div>
  <div class="abs web">www.qnacademyga.com</div>
  <div class="abs phone">555-014-2287</div>
</main>
</body>
</html>
```